Verdana Glen Website

I need a design of homepage for a health and wellness center. We considers self to be young and fresh and want something along that design. We want a main picture/logo/design (or all three), and underneath that 4 pictures to depict what services we do. The four services are Orthopedic Rehab, Neurological Rehab, Speech Pathology and Float. I have attached our logo, and some pictures that might be helpful, but the pictures don't have to be included. Here is an example of what I would like it look. http://pixelquarry.com/web-design/contests/brimlotts-website-design-needed-more-work-come-submit-517306/entries/84162975

Health

```html
<!DOCTYPE html>
<html lang="en">
<head>
<meta charset="utf-8">
<title>Verdana Glen – Health and Wellness</title>
<link rel="stylesheet" href="https://fonts.googleapis.com/css2?family=Open+Sans:wght@400;600;700;800&family=Roboto+Condensed:wght@400;700&display=swap">
<style>
:root{
  --page:#e4e5e6;
  --sheet:#ffffff;
  --topbar:#3a3b3d;
  --header:#2e2f31;
  --nav-line:#4a4b4e;
  --green:#8cc63f;
  --green-dark:#5f9a1c;
  --ink:#333537;
  --muted:#7b7d80;
  --soft:#f3f4f4;
  --rule:#d5d6d8;
  --footer:#2b2c2e;
  --footer-text:#b9bbbe;
}
*{box-sizing:border-box;margin:0;padding:0}
html,body{width:863px;height:1200px;overflow:hidden}
body{background:var(--page);font-family:"Open Sans",Arial,sans-serif;color:var(--ink);position:relative}

.top-bar{position:absolute;left:0;top:0;width:863px;height:23px;background:var(--topbar);display:flex;align-items:center;justify-content:space-between;padding:0 30px;font-size:10px;color:#cfd0d2}
.top-links{display:flex;gap:22px}
.top-social{display:flex;gap:6px;align-items:center}
.top-social span{width:11px;height:11px;background:#8e9093;display:block}

.site-header{position:absolute;left:0;top:23px;width:863px;height:115px;background:var(--header)}
.brand{position:absolute;left:40px;top:58px;font-size:26px;font-weight:600;color:#fff;line-height:1}
.main-nav{position:absolute;right:30px;top:72px;display:flex;height:34px}
.main-nav a{display:flex;align-items:center;padding:0 14px;font-size:11px;color:#e7e8e9;text-decoration:none;border-left:1px solid var(--nav-line)}
.main-nav a:first-child{border-left:none}
.main-nav a.active{background:var(--green);color:#fff}

.sheet{position:absolute;left:24px;top:138px;width:815px;height:937px;background:var(--sheet)}

.hero{position:absolute;left:10px;top:14px;width:795px;height:322px;background:linear-gradient(180deg,#f7f8f8,#e7e9ea);border:1px solid var(--rule)}
.hero-visual{position:absolute;right:14px;top:16px;width:410px;height:270px;border-radius:6px;background:radial-gradient(circle at 62% 48%,#cfe8b0 0,#e2eedb 35%,#eef0ef 70%)}
.hero-copy{position:absolute;left:28px;top:48px;width:340px}
.hero-title{font-size:38px;font-weight:800;color:var(--green);line-height:1;white-space:nowrap}
.hero-sub{font-size:17px;font-weight:800;color:var(--ink);margin-top:10px;white-space:nowrap}
.hero-text{font-size:11px;line-height:1.4;color:var(--muted);margin-top:8px}
.btn{display:inline-block;background:var(--green);color:#fff;text-decoration:none;font-weight:600;border-radius:3px}
.hero .btn{margin-top:30px;font-size:13px;padding:9px 26px}
.hero-dots{position:absolute;left:385px;bottom:16px;display:flex;gap:6px}
.hero-dots span{width:8px;height:8px;border-radius:50%;background:#9a9c9f}
.hero-dots span.on{background:var(--green-dark)}

.intro{position:absolute;left:0;top:366px;width:815px;text-align:center}
.intro h1{font-family:"Roboto Condensed",Arial,sans-serif;font-weight:400;font-size:27px;color:#55575a}
.intro p{width:650px;margin:10px auto 0;font-size:10px;line-height:1.5;color:var(--muted)}

.services{position:absolute;left:0;top:510px;width:815px;display:flex;justify-content:space-around;padding:0 20px}
.service{width:170px;text-align:center}
.service-icon{width:126px;height:126px;border-radius:50%;background:var(--soft);border:1px solid var(--rule);margin:0 auto;display:flex;align-items:center;justify-content:center}
.icon-fill{width:78px;height:78px;border-radius:10px;background:linear-gradient(160deg,#9fd159,#5f9a1c)}
.service h2{font-size:14px;font-weight:600;color:var(--ink);margin-top:20px}
.service p{font-size:10px;line-height:1.45;color:var(--muted);margin-top:6px}
.service .btn{font-size:10px;padding:5px 16px;margin-top:14px}

.partners{position:absolute;left:0;top:848px;width:815px;height:80px;border-top:1px solid var(--rule);display:flex;align-items:center;justify-content:space-around;padding:0 24px}
.partner{height:26px;border-radius:3px;background:#bfc1c4}

.site-footer{position:absolute;left:0;top:1080px;width:863px;height:120px;background:var(--footer);color:var(--footer-text);font-size:10px}
.footer-accent{height:4px;background:linear-gradient(90deg,var(--green),#4aa7c9,var(--green))}
.connect{position:absolute;left:24px;top:20px}
.connect h3{font-size:14px;font-weight:600;color:#fff}
.social-list{display:flex;gap:22px;margin-top:22px}
.social-list span{display:flex;align-items:center;gap:6px}
.social-list i{width:16px;height:16px;background:#8e9093;display:block}
.footer-nav{position:absolute;right:30px;top:50px;display:flex;gap:8px}
.footer-nav a{color:var(--footer-text);text-decoration:none}
.copyright{position:absolute;right:30px;top:72px;color:#7f8184;font-size:9px}
</style>
</head>
<body>

<div class="top-bar">
  <div class="top-links"><span>All Previews</span><span>Archives</span><span>Contact Us</span></div>
  <div class="top-social"><span></span><span></span><span></span><span></span></div>
</div>

<header class="site-header">
  <div class="brand">Verdana Glen</div>
  <nav class="main-nav">
    <a href="#">Home</a>
    <a href="#">About Us</a>
    <a href="#" class="active">Health facts</a>
    <a href="#">Sugar free</a>
    <a href="#">Contact Us</a>
  </nav>
</header>

<main class="sheet">
  <section class="hero">
    <div class="hero-visual" role="img" aria-label="Soft green wellness artwork with floating cubes"></div>
    <div class="hero-copy">
      <div class="hero-title">LOREM IPSUM.</div>
      <div class="hero-sub">CONSECTETUER FDADPISCING.</div>
      <p class="hero-text">It is a long established fact that a reader will be distracted by the readable content of a page when looking at its layout. The point of using Lorem.</p>
      <a class="btn" href="#">Learn More</a>
    </div>
    <div class="hero-dots"><span class="on"></span><span></span><span></span><span></span></div>
  </section>

  <section class="intro">
    <h1>Coning elitufere eu mas. Quisq dipibuque fermen tum.</h1>
    <p>Donec suscipit vehicula turpis sed lobortis quisque vitae quam neque. Morbi ultrices placerat dapibus etiam ultricies nulla vel leo malesuada commodo bibendum orci in tortor. Donec suscipit vehicula turpis sed lobortis quisque vitae quam neque. Morbi ultrices placerat dapibus etiam ultricies nulla vel leo malesuada commodo lit.</p>
  </section>

  <section class="services">
    <article class="service">
      <div class="service-icon"><div class="icon-fill" role="img" aria-label="Medical staff emblem for orthopedic rehab"></div></div>
      <h2>Orthopedic Rehab.</h2>
      <p>It is a long established fact that a reader will be distracted by the readable content</p>
      <a class="btn" href="#">Read More</a>
    </article>
    <article class="service">
      <div class="service-icon"><div class="icon-fill" role="img" aria-label="Clinician figure for neurological rehab"></div></div>
      <h2>Neurological Rehab.</h2>
      <p>It is a long established fact that a reader will be distracted by the readable content</p>
      <a class="btn" href="#">Read More</a>
    </article>
    <article class="service">
      <div class="service-icon">
        <svg width="80" height="70" viewBox="0 0 80 70" aria-hidden="true">
          <rect x="28" y="4" width="24" height="12" rx="3" fill="none" stroke="#333537" stroke-width="5"/>
          <rect x="4" y="14" width="72" height="52" rx="8" fill="#333537"/>
          <rect x="34" y="26" width="12" height="30" fill="#fff"/>
          <rect x="25" y="35" width="30" height="12" fill="#fff"/>
        </svg>
      </div>
      <h2>Speech Pathology</h2>
      <p>It is a long established fact that a reader will be distracted by the readable content</p>
      <a class="btn" href="#">Read More</a>
    </article>
    <article class="service">
      <div class="service-icon">
        <svg width="78" height="78" viewBox="0 0 78 78" aria-hidden="true">
          <rect x="26" y="2" width="26" height="74" fill="#333537"/>
          <rect x="2" y="26" width="74" height="26" fill="#333537"/>
          <rect x="30" y="6" width="18" height="66" fill="var(--green)"/>
          <rect x="6" y="30" width="66" height="18" fill="var(--green)"/>
        </svg>
      </div>
      <h2>Float</h2>
      <p>It is a long established fact that a reader will be distracted by the readable content</p>
      <a class="btn" href="#">Read More</a>
    </article>
  </section>

  <section class="partners" aria-label="Partners">
    <div class="partner" style="width:80px"></div>
    <div class="partner" style="width:70px"></div>
    <div class="partner" style="width:95px"></div>
    <div class="partner" style="width:95px"></div>
    <div class="partner" style="width:105px"></div>
    <div class="partner" style="width:75px"></div>
    <div class="partner" style="width:90px"></div>
  </section>
</main>

<footer class="site-footer">
  <div class="footer-accent"></div>
  <div class="connect">
    <h3>Connect with us</h3>
    <div class="social-list">
      <span><i></i>Chirpline</span>
      <span><i></i>Linkwell</span>
      <span><i></i>Viewcast</span>
    </div>
  </div>
  <nav class="footer-nav">
    <a href="#">Home</a>|<a href="#">About Us</a>|<a href="#">Services</a>|<a href="#">Contact Us</a>|<a href="#">Terms &amp; Conditions</a>|<a href="#">Sitemap</a>
  </nav>
  <div class="copyright">© 2024 Verdana Glen. All rights reserved.</div>
</footer>

</body>
</html>
```